Business Folder

I need a fresh, modern design for a business folder. I have our company's colors, logo, and a separate file for just the graphic part of our logo as a design element. No photo, just colors, gradients, and shadows to create depth. I like the idea of a rich grey as the background, however, I realize we'd have to lighten to 'Tax Advisory Services' part of our logo.

The design would just be the 'front' or outside of the folder from Mellowfax. Design file attached. You can find that here under 9 x 12 standard folder, Left and Right Pockets With Slit Both Sides:

https://www.mellowfax-example.com/content.html?id=folderDownloadTemplates&rightMenuId=rightMenu&footerId=bodyFooterStyle6

```html
<!DOCTYPE html>
<html lang="en">
<head>
<meta charset="utf-8">
<title>Corvane Business Folder – Outside Spread</title>
<link rel="stylesheet" href="https://fonts.googleapis.com/css2?family=Lato:wght@400;700;900&display=swap">
<style>
  :root {
    --backdrop: #e4e5e7;
    --paper: #ffffff;
    --navy: #0a4478;
    --navy-deep: #073a66;
    --blue-mid: #0d6fa6;
    --teal: #1797b8;
    --teal-light: #2fb1cc;
    --brand-blue: #1f5a92;
    --photo-light: #dfe6ec;
    --photo-mid: #a9b8c6;
    --photo-dark: #5d6b78;
  }
  * { box-sizing: border-box; margin: 0; padding: 0; }
  html, body {
    width: 1200px;
    height: 847px;
    overflow: hidden;
    background: var(--backdrop);
    font-family: "Lato", Arial, sans-serif;
  }
  .folder-spread {
    position: absolute;
    left: 30px;
    top: 43px;
    width: 1140px;
    height: 760px;
    display: flex;
    box-shadow: 0 10px 30px rgba(0,0,0,0.18);
  }
  .folder-panel {
    position: relative;
    width: 570px;
    height: 760px;
    background: var(--paper);
    overflow: hidden;
  }
  .folder-panel svg.panel-art {
    position: absolute;
    inset: 0;
    width: 100%;
    height: 100%;
  }
  .back-address {
    position: absolute;
    left: 0;
    right: 0;
    bottom: 70px;
    text-align: center;
    color: var(--paper);
    font-size: 14px;
    line-height: 1.35;
  }
  .back-address .address-label {
    font-size: 17px;
    font-weight: 700;
    margin-bottom: 2px;
  }
  .front-wordmark {
    position: absolute;
    top: 70px;
    left: 0;
    right: 0;
    text-align: center;
    font-size: 62px;
    font-weight: 900;
    letter-spacing: 2px;
    color: var(--brand-blue);
  }
</style>
</head>
<body>
  <main class="folder-spread">
    <section class="folder-panel folder-back">
      <svg class="panel-art" viewBox="0 0 570 760" preserveAspectRatio="none" aria-hidden="true">
        <defs>
          <linearGradient id="back-navy" x1="0" y1="0" x2="1" y2="1">
            <stop offset="0" stop-color="#0b4f86"/>
            <stop offset="1" stop-color="#073a66"/>
          </linearGradient>
        </defs>
        <path class="swoosh-teal" d="M0 230 C 80 130, 260 50, 570 30 L 570 60 C 330 70, 130 150, 0 270 Z" fill="var(--teal)"/>
        <path class="swoosh-light" d="M120 150 C 220 90, 330 60, 420 45 C 320 70, 220 110, 150 150 Z" fill="var(--teal-light)"/>
        <path class="swoosh-blue" d="M0 260 C 120 150, 330 70, 570 55 L 570 80 C 360 90, 150 170, 0 300 Z" fill="var(--blue-mid)"/>
        <path class="body-navy" d="M0 300 C 150 170, 360 90, 570 80 L 570 760 L 0 760 Z" fill="url(#back-navy)"/>
      </svg>
      <address class="back-address">
        <div class="address-label">Address:</div>
        Lorem ipsum dolor sit amet, consectetuer adipisc-<br>
        ing elit, sed diam nonummy nibh<br>
        Ph: 0000 000 000, Fax: 0000 000 000
      </address>
    </section>

    <section class="folder-panel folder-front">
      <svg class="panel-art" viewBox="0 0 570 760" preserveAspectRatio="none">
        <defs>
          <linearGradient id="photo-fill" x1="0" y1="0" x2="0.6" y2="1">
            <stop offset="0" stop-color="var(--photo-light)"/>
            <stop offset="0.5" stop-color="var(--photo-mid)"/>
            <stop offset="1" stop-color="var(--photo-dark)"/>
          </linearGradient>
          <linearGradient id="band-fill" x1="0" y1="0" x2="1" y2="0">
            <stop offset="0" stop-color="#1a8fb2"/>
            <stop offset="1" stop-color="#14a2c2"/>
          </linearGradient>
        </defs>
        <path class="office-photo" role="img" aria-label="Office desk photo with reading glasses on printed charts, laptop and keyboard, blurred colleagues in a bright room"
              d="M0 200 C 120 300, 260 360, 390 360 C 470 360, 530 330, 570 300 L 570 760 L 0 760 Z" fill="url(#photo-fill)"/>
        <path class="wave-band" d="M0 150 C 120 260, 260 320, 390 320 C 470 320, 530 290, 570 250 L 570 300 C 530 330, 470 360, 390 360 C 260 360, 120 300, 0 200 Z" fill="url(#band-fill)"/>
      </svg>
      <div class="front-wordmark">CORVANE</div>
    </section>
  </main>
</body>
</html>
```